Tomas's Business Cards

My husband is a self employed Cabinet Maker... who contracts to Building companies and clients directly.
He installs kitchesn, designs and also completes renovations and building work.

I would like a small, FUNKY, simple but eye catching design.

It needs to incorporate the following.
Custom Cabinets / Installations / Renovations / Design

Commercial and Residential

He does not have a Website or Chatterly,
contact number is 0438 207 619 and email is tomasvelkin@quillmail.example

I would like a Grey/Silver on black, or blue covering.. I am open to colour designs?

Thank you. :-)

Target Market(s)

Building Companies
Clients
Other Trades people onsite,. to give out at job sites

Industry/Entity Type

Business

Contact Information for Business Card

Phone: 0438 207 619
Email: tomasvelkin@quillmail.example

Font styles to use
Sans Serif

Colors
0592cd
747474
474747
1b1b1b
85cae6

Requirements
Must have
• Funky, simple, eye catching design
• Would like use of Silver/Grey - and a colour that would complement this.
• Am open to ideas :-)
Nice to have
• We do not have a logo or picture, will leave this up to you if you think an image would be beneficial???
• Thank you.

```html
<!DOCTYPE html>
<html lang="en">
<head>
<meta charset="UTF-8">
<title>Tomas Velkin – Business Card</title>
<link href="https://fonts.googleapis.com/css2?family=Lato:wght@300;400;700&display=swap" rel="stylesheet">
<style>
  :root {
    --backdrop: #474747;
    --card-deep: #1a2a9e;
    --card-mid: #1d4fc8;
    --card-glow: #1e8fe6;
    --band: #0b0b0b;
    --ink: #ffffff;
  }
  * { margin: 0; padding: 0; box-sizing: border-box; }
  html, body {
    width: 1200px;
    height: 900px;
    overflow: hidden;
    background: var(--backdrop);
    font-family: "Lato", sans-serif;
  }
  .canvas {
    position: relative;
    width: 1200px;
    height: 900px;
  }
  .card {
    position: absolute;
    left: 100px;
    top: 145px;
    width: 1000px;
    height: 611px;
    border-radius: 34px;
    overflow: hidden;
    box-shadow: 0 24px 50px rgba(0, 0, 0, 0.45);
  }
  .card-texture {
    position: absolute;
    inset: 0;
    background:
      radial-gradient(ellipse 55% 60% at 62% 42%, var(--card-glow) 0%, rgba(30, 143, 230, 0) 70%),
      linear-gradient(160deg, var(--card-mid) 0%, var(--card-deep) 100%);
  }
  .band {
    position: absolute;
    left: 0;
    background: var(--band);
    color: var(--ink);
    display: flex;
    align-items: center;
    white-space: nowrap;
  }
  .name-band {
    top: 100px;
    width: 560px;
    height: 86px;
    padding-left: 78px;
    font-size: 54px;
    font-weight: 300;
    letter-spacing: 0.5px;
  }
  .name-band .surname { font-weight: 700; margin-left: 14px; }
  .contact-band {
    height: 42px;
    padding-left: 78px;
    font-size: 27px;
    font-weight: 400;
  }
  .phone { top: 264px; width: 430px; }
  .email { top: 309px; width: 600px; }
  .services {
    position: absolute;
    right: 70px;
    top: 420px;
    text-align: right;
    color: var(--ink);
    font-weight: 700;
    font-size: 29px;
    letter-spacing: 0.6px;
    text-transform: uppercase;
    line-height: 62px;
  }
  .services .dot {
    display: inline-block;
    width: 20px;
    height: 20px;
    border-radius: 50%;
    background: var(--ink);
    margin: 0 14px;
    vertical-align: 2px;
  }
</style>
</head>
<body>
  <main class="canvas">
    <section class="card">
      <div class="card-texture" role="img" aria-label="Blue background with a pattern of translucent overlapping rounded squares"></div>

      <h1 class="band name-band"><span class="given">Tomas</span><span class="surname">Velkin</span></h1>

      <p class="band contact-band phone">Phone: 0438 207 619</p>
      <p class="band contact-band email">Email: tomasvelkin@quillmail.example</p>

      <div class="services">
        <p>Custom Cabinets<span class="dot"></span>Installations</p>
        <p>Renovations<span class="dot"></span>Design Commercial and Residential</p>
      </div>
    </section>
  </main>
</body>
</html>
```